Microblading website contest - Make it colorful

Beauty salon focusing on microblading need a better website template. Please make a 1 page site mobile optimized and nicer layout with better color formulation. Would love interactive images in the site. You can use stock images and if approve we can pay for it.
Current site:
tessawynkelpeony.com

Inspiration:
https://framqueue.net/shots/41877260-Microblading-HomePage
https://framqueue.net/shots/7914026-Lunetto-Microblading-Eyebrow-Beauty-Salon-Pagewright-Theme

Target Market(s)

women

Industry/Entity Type

beauty salon

Number of Pages Required

1 page

Font styles to use
Serif
Decorative
Script

Requirements
Nice to have
• As pretty as possible

```html
<!DOCTYPE html>
<html lang="en">
<head>
<meta charset="utf-8">
<title>Peony Brows Tessa – Microblading</title>
<link href="https://fonts.googleapis.com/css2?family=PT+Serif:wght@400;700&family=Poppins:wght@400;500;600&display=swap" rel="stylesheet">
<style>
:root{
  --orange:#d5822f;
  --peach:#fde6c3;
  --cream:#fef3e0;
  --ink:#161616;
  --grey:#8a8a8a;
  --white:#ffffff;
  --black:#0e0e0e;
}
*{margin:0;padding:0;box-sizing:border-box}
html,body{width:1200px;height:4208px;overflow:hidden}
body{font-family:"PT Serif",serif;color:var(--ink);background:var(--white);position:relative}
.abs{position:absolute}
.btn{position:absolute;background:var(--orange);color:var(--white);font-family:"PT Serif",serif;font-weight:700;font-size:15px;display:flex;align-items:center;justify-content:center;box-shadow:0 8px 18px rgba(213,130,47,.25)}
.label{font-size:19px;text-transform:uppercase;letter-spacing:.3px}
.heading{font-size:34px;font-weight:700}

/* hero */
.hero{position:absolute;left:0;top:0;width:1200px;height:583px;
  background:
    radial-gradient(ellipse 260px 200px at 330px 90px,rgba(235,215,200,.75),rgba(235,215,200,0) 70%),
    radial-gradient(ellipse 380px 300px at 120px 470px,rgba(70,40,22,.8),rgba(70,40,22,0) 70%),
    radial-gradient(ellipse 300px 260px at 1000px 180px,rgba(190,150,120,.7),rgba(190,150,120,0) 70%),
    radial-gradient(ellipse 240px 160px at 1070px 340px,rgba(40,28,24,.75),rgba(40,28,24,0) 70%),
    radial-gradient(ellipse 420px 320px at 640px 380px,rgba(214,150,92,.6),rgba(214,150,92,0) 70%),
    linear-gradient(110deg,#8a5a34 0%,#b07443 40%,#c4884f 60%,#93603a 100%)}
.brand{left:116px;top:28px;color:var(--white);font-size:20px;font-weight:700}
.nav{left:438px;top:32px;display:flex;gap:33px;color:var(--white);font-size:14px;font-weight:700}
.hero-title{left:0;width:1200px;top:236px;text-align:center;color:var(--white);font-size:62px;font-weight:400}
.hero-sub{left:0;width:1200px;top:325px;text-align:center;color:#f6e6d6;font-size:19px}

/* about */
.photo{position:absolute;box-shadow:0 14px 30px rgba(0,0,0,.18)}
.about-text{left:516px;top:650px;width:594px}
.about-text h2{font-size:34px;margin:14px 0 20px;line-height:1.2}
.about-text h2 span{color:var(--orange)}
.about-text p,.about-text li{font-size:19px;line-height:30px}
.about-text ul{padding-left:30px}

/* why */
.why{left:0;top:1243px;width:1200px;height:707px;background:var(--peach)}
.why-intro{left:116px;top:1318px;width:620px}
.why-intro p{font-size:19px;line-height:30px;margin-top:14px}
.feature{position:absolute;width:266px;background:var(--white);border-top:3px solid var(--orange);padding:34px 34px;font-family:"Poppins",sans-serif;box-shadow:0 12px 30px rgba(0,0,0,.05)}
.feature svg{display:block;margin-bottom:26px}
.feature h3{font-size:20px;font-weight:500;line-height:30px;margin-bottom:14px}
.feature p{font-size:12px;color:#666;line-height:20px}

/* services */
.services-head{left:115px;top:2015px;width:960px}
.services-head .label{text-decoration:underline;text-underline-offset:4px}
.services-head p{color:var(--grey);font-size:19px;line-height:30px;margin-top:14px}
.service{position:absolute;top:2212px;width:300px;height:183px;background:var(--white);padding:16px 16px;box-shadow:0 14px 30px rgba(0,0,0,.1)}
.service h3{font-size:26px;font-weight:700;margin-bottom:6px}
.service p{color:var(--grey);font-size:19px;line-height:30px}
.tag{position:absolute;left:16px;bottom:16px;border:1.5px solid var(--orange);color:var(--orange);font-size:13px;padding:5px 18px}

/* gallery */
.gallery{left:0;top:2565px;width:1200px;height:740px;background:var(--cream)}
.center{left:0;width:1200px;text-align:center}
.tile{position:absolute}
.tile-caption{position:absolute;left:0;right:0;bottom:16px;text-align:center;color:var(--white);font-weight:700;font-size:20px}

/* testimonials */
.arrow{position:absolute;top:3380px;width:66px;height:66px;border-radius:50%;display:flex;align-items:center;justify-content:center}
.review{position:absolute;top:3478px;width:467px;height:300px;padding:34px 51px;box-shadow:0 14px 30px rgba(0,0,0,.1)}
.review .who{display:flex;align-items:center;gap:20px}
.avatar{width:82px;height:82px;border-radius:50%}
.review h4{color:var(--orange);font-size:27px;font-weight:700}
.review p{width:345px;font-size:19px;line-height:24px;margin:24px 0 14px}
.stars{display:flex;gap:16px}

/* footer */
.footer{left:0;top:3848px;width:1200px;height:360px;background:var(--black);color:var(--white)}
.footer h3{font-size:27px;font-weight:700}
.social{left:115px;top:70px}
.social ul{list-style:none;margin-top:18px}
.social li{font-size:15px;line-height:33px}
.subscribe{left:387px;top:70px}
.subscribe p{font-size:15px;margin-top:6px}
.email{left:387px;top:152px;width:466px;height:50px;background:var(--white);color:#aaa;font-size:17px;padding:12px 16px}
.rule{left:115px;top:282px;width:968px;height:1px;background:#ddd}
.copy{left:0;width:1200px;top:310px;text-align:center;font-size:18px}
</style>
</head>
<body>

<header class="hero" role="img" aria-label="Photo of the brow artist in glasses and a mask at work, warm toned"></header>
<div class="abs brand">Microblading</div>
<nav class="abs nav"><span>Home</span><span>About</span><span>Services</span><span>Gallery</span><span>Shop</span><span>Academy</span><span>Contact us</span><span>More</span></nav>
<h1 class="abs hero-title">- Peony Brows Tessa -</h1>
<p class="abs hero-sub">&gt;&gt;&gt; Your personal eyebrow specialist</p>
<div class="btn" style="left:510px;top:378px;width:181px;height:48px">See More</div>

<section>
  <div class="photo" role="img" aria-label="Artist working on a client's brows" style="left:80px;top:698px;width:195px;height:232px;background:radial-gradient(ellipse 90px 70px at 130px 70px,#1e1e1e,rgba(30,30,30,0) 75%),radial-gradient(ellipse 80px 60px at 60px 180px,#3a3838,rgba(58,56,56,0) 75%),linear-gradient(160deg,#e4e0dc,#a9a29d 55%,#5a5450)"></div>
  <div class="photo" role="img" aria-label="Artist in a white coat at a treatment bed" style="left:80px;top:938px;width:195px;height:232px;background:radial-gradient(ellipse 60px 70px at 110px 110px,#2a2a2a,rgba(42,42,42,0) 75%),radial-gradient(ellipse 110px 60px at 100px 200px,#f2f0ee,rgba(242,240,238,0) 75%),linear-gradient(150deg,#d8d2cc,#9b938d 60%,#6e6661)"></div>
  <div class="photo" role="img" aria-label="Client in a hair cap receiving treatment" style="left:288px;top:650px;width:195px;height:230px;background:radial-gradient(ellipse 70px 60px at 60px 80px,#e9eef2,rgba(233,238,242,0) 75%),radial-gradient(ellipse 70px 80px at 150px 150px,#1d1d1d,rgba(29,29,29,0) 75%),linear-gradient(140deg,#efe9e3,#c8b8aa 55%,#8d8078)"></div>
  <div class="photo" role="img" aria-label="Academy graduates with gold and black balloons" style="left:288px;top:890px;width:195px;height:232px;background:radial-gradient(circle 40px at 40px 40px,#c9a843,rgba(201,168,67,0) 80%),radial-gradient(circle 40px at 150px 30px,#d8b64e,rgba(216,182,78,0) 80%),radial-gradient(circle 35px at 100px 60px,#1a1a1a,rgba(26,26,26,0) 80%),radial-gradient(ellipse 100px 60px at 100px 170px,#222,rgba(34,34,34,0) 80%),linear-gradient(180deg,#7a6634,#3b342a 60%,#8a6a3a)"></div>
  <div class="abs about-text">
    <div class="label">About us</div>
    <h2>Peony Brows, Tessa PMU - <span>Beauty Academy</span></h2>
    <p>All color cream, needle piece and tools are EU certificated.</p>
    <ul>
      <li>We use disposable needles during the full process.</li>
      <li>Fineline color cream: Germany's largest brand. It does not contain heavy metals. Their color stabilizer prevents any discoloration by time.</li>
      <li>PMU technique. Maintains 1-2 year +</li>
      <li>Hand-draw every individual hair as if it is your real eyebrow. By using a very fine and soft needle implanting pigment under the skin.</li>
      <li>No awkward recovering time. Leave with a fresh, beautiful, new look!</li>
    </ul>
  </div>
</section>

<section>
  <div class="abs why"></div>
  <div class="abs why-intro">
    <div class="label">Why choose us</div>
    <h2 class="heading" style="margin-top:18px">Your Eyebrows and Beauty</h2>
    <p>Once the eyebrow is designed, your eyebrow will become a finishing touch of the face. Brings your beauty to an upper level.</p>
  </div>
  <div class="abs" role="img" aria-label="Portrait of the smiling brow artist in a white top" style="left:140px;top:1505px;width:320px;height:445px;background:radial-gradient(ellipse 120px 150px at 160px 120px,#2b2420,rgba(43,36,32,0) 78%),radial-gradient(ellipse 70px 90px at 160px 130px,#f1d3bd,rgba(241,211,189,0) 80%),radial-gradient(ellipse 150px 130px at 165px 380px,#fbfaf8,rgba(251,250,248,0) 80%),radial-gradient(ellipse 60px 160px at 80px 300px,#2b2420,rgba(43,36,32,0) 80%)"></div>
  <div class="feature" style="left:526px;top:1608px;height:272px">
    <svg width="38" height="36" viewBox="0 0 24 23"><path fill="#d5822f" d="M12 0l3.1 7.6 8.2.6-6.3 5.3 2 8L12 17.2 5 21.5l2-8L.7 8.2l8.2-.6z"/></svg>
    <h3>Licensed<br>microblading artist</h3>
    <p>License from various states in United State</p>
  </div>
  <div class="feature" style="left:820px;top:1465px;height:271px">
    <svg width="38" height="36" viewBox="0 0 24 23"><path fill="#d5822f" d="M12 0l3.1 7.6 8.2.6-6.3 5.3 2 8L12 17.2 5 21.5l2-8L.7 8.2l8.2-.6z"/></svg>
    <h3>Years of<br>experience</h3>
    <p>Over thousands of cases and Oversea study and practice</p>
  </div>
  <div class="feature" style="left:820px;top:1755px;height:270px">
    <svg width="38" height="36" viewBox="0 0 24 23"><path fill="#d5822f" d="M12 0l3.1 7.6 8.2.6-6.3 5.3 2 8L12 17.2 5 21.5l2-8L.7 8.2l8.2-.6z"/></svg>
    <h3>European latest<br>technique</h3>
    <p>We study European-style natural hair flow, improve and make it suitable for Asians</p>
  </div>
</section>

<section>
  <div class="abs services-head">
    <div class="label">Services</div>
    <h2 class="heading" style="margin-top:22px">Specialized service</h2>
    <p>We treat every client as our friends and family. We give you the most sincere advise and best quality and service.</p>
  </div>
  <div class="service" style="left:115px"><h3>Natural Brows</h3><p>Microblading | Hand-drawing hair lines</p><span class="tag">For all skin type</span></div>
  <div class="service" style="left:448px"><h3>Hair Stroke</h3><p>Trendy | Machine-draw line | No wounds</p><span class="tag">For all skin type</span></div>
  <div class="service" style="left:781px"><h3>Powder Brows</h3><p>Powder effect | Light, matt gradient</p><span class="tag">For all skin type</span></div>
  <div class="btn" style="left:507px;top:2450px;width:182px;height:48px">See More</div>
</section>

<section>
  <div class="abs gallery"></div>
  <div class="abs center label" style="top:2632px">Our gallery</div>
  <h2 class="abs center heading" style="top:2670px">FineLine Academy Course</h2>
  <div class="tile" role="img" aria-label="Students in a classroom" style="left:116px;top:2736px;width:300px;height:132px;background:radial-gradient(ellipse 90px 40px at 200px 40px,#e9eef2,rgba(233,238,242,0) 80%),radial-gradient(ellipse 120px 40px at 150px 115px,#2a2724,rgba(42,39,36,0) 80%),linear-gradient(180deg,#cfcbc6,#8d8782 55%,#4c4844)"></div>
  <div class="tile" role="img" aria-label="Student practising brow drawing" style="left:116px;top:2913px;width:300px;height:222px;background:radial-gradient(ellipse 100px 80px at 220px 60px,#2a2420,rgba(42,36,32,0) 80%),radial-gradient(ellipse 120px 80px at 110px 170px,#7d7358,rgba(125,115,88,0) 80%),linear-gradient(150deg,#e6ddd3,#b9aa9b 55%,#6d6259)"></div>
  <div class="tile" role="img" aria-label="Graduates celebrating with balloons" style="left:450px;top:2736px;width:300px;height:399px;background:radial-gradient(circle 60px at 60px 50px,#c9a843,rgba(201,168,67,0) 80%),radial-gradient(circle 60px at 240px 40px,#d8b64e,rgba(216,182,78,0) 80%),radial-gradient(circle 50px at 150px 70px,#151515,rgba(21,21,21,0) 80%),radial-gradient(ellipse 150px 90px at 150px 220px,#1c1c1c,rgba(28,28,28,0) 80%),linear-gradient(180deg,#7b6a3c,#3a3328 55%,#c07a36)"><span class="tile-caption">Graduate Celebration</span></div>
  <div class="tile" role="img" aria-label="Student treating a client in a hair cap" style="left:783px;top:2736px;width:300px;height:222px;background:radial-gradient(ellipse 80px 60px at 80px 140px,#eef1f4,rgba(238,241,244,0) 80%),radial-gradient(ellipse 110px 100px at 210px 120px,#1d1d1d,rgba(29,29,29,0) 80%),linear-gradient(170deg,#cfd6dc,#8a8d90 55%,#3d3d3d)"></div>
  <div class="tile" role="img" aria-label="Artist demonstrating technique" style="left:783px;top:3002px;width:300px;height:133px;background:radial-gradient(ellipse 90px 50px at 90px 70px,#1a1a1e,rgba(26,26,30,0) 80%),radial-gradient(ellipse 80px 50px at 230px 50px,#b7a58a,rgba(183,165,138,0) 80%),linear-gradient(135deg,#a9abb2,#5a5b60 55%,#2a2a2e)"></div>
  <div class="btn" style="left:509px;top:3189px;width:182px;height:49px">See More</div>
</section>

<section>
  <div class="abs label" style="left:116px;top:3376px">Testimonials</div>
  <h2 class="abs heading" style="left:116px;top:3414px">What Our Clients Say</h2>
  <div class="arrow" style="left:930px;background:#ececec"><svg width="26" height="26" viewBox="0 0 24 24" fill="none" stroke="#aaa" stroke-width="2"><path d="M20 12H4M10 6l-6 6 6 6"/></svg></div>
  <div class="arrow" style="left:1016px;background:var(--peach)"><svg width="26" height="26" viewBox="0 0 24 24" fill="none" stroke="#d5822f" stroke-width="2"><path d="M4 12h16M14 6l6 6-6 6"/></svg></div>
  <div class="review" style="left:116px;background:var(--white)">
    <div class="who"><div class="avatar" role="img" aria-label="Client portrait" style="background:radial-gradient(ellipse 26px 40px at 41px 44px,#3a302a,rgba(58,48,42,0) 85%),#e9e9e9"></div><h4>Mara L.</h4></div>
    <p style="color:var(--grey)">This is my first time getting micro-blading eyebrows and writing a review Excelent job both eyebrows and eyelid lifting done by Tessa.</p>
    <div class="stars">
      <svg width="22" height="21" viewBox="0 0 24 23"><path fill="#d5822f" d="M12 0l3.1 7.6 8.2.6-6.3 5.3 2 8L12 17.2 5 21.5l2-8L.7 8.2l8.2-.6z"/></svg><svg width="22" height="21" viewBox="0 0 24 23"><path fill="#d5822f" d="M12 0l3.1 7.6 8.2.6-6.3 5.3 2 8L12 17.2 5 21.5l2-8L.7 8.2l8.2-.6z"/></svg><svg width="22" height="21" viewBox="0 0 24 23"><path fill="#d5822f" d="M12 0l3.1 7.6 8.2.6-6.3 5.3 2 8L12 17.2 5 21.5l2-8L.7 8.2l8.2-.6z"/></svg><svg width="22" height="21" viewBox="0 0 24 23"><path fill="#d5822f" d="M12 0l3.1 7.6 8.2.6-6.3 5.3 2 8L12 17.2 5 21.5l2-8L.7 8.2l8.2-.6z"/></svg><svg width="22" height="21" viewBox="0 0 24 23"><path fill="#d5822f" d="M12 0l3.1 7.6 8.2.6-6.3 5.3 2 8L12 17.2 5 21.5l2-8L.7 8.2l8.2-.6z"/></svg>
    </div>
  </div>
  <div class="review" style="left:616px;background:var(--cream)">
    <div class="who"><div class="avatar" role="img" aria-label="Client portrait" style="background:radial-gradient(ellipse 26px 34px at 46px 46px,#d9a98a,rgba(217,169,138,0) 85%),#c9363c"></div><h4>Nina K.</h4></div>
    <p>This is my first time getting micro-blading eyebrows and writing a review Excelent job both eyebrows and eyelid lifting done by Tessa.</p>
    <div class="stars">
      <svg width="22" height="21" viewBox="0 0 24 23"><path fill="#d5822f" d="M12 0l3.1 7.6 8.2.6-6.3 5.3 2 8L12 17.2 5 21.5l2-8L.7 8.2l8.2-.6z"/></svg><svg width="22" height="21" viewBox="0 0 24 23"><path fill="#d5822f" d="M12 0l3.1 7.6 8.2.6-6.3 5.3 2 8L12 17.2 5 21.5l2-8L.7 8.2l8.2-.6z"/></svg><svg width="22" height="21" viewBox="0 0 24 23"><path fill="#d5822f" d="M12 0l3.1 7.6 8.2.6-6.3 5.3 2 8L12 17.2 5 21.5l2-8L.7 8.2l8.2-.6z"/></svg><svg width="22" height="21" viewBox="0 0 24 23"><path fill="#d5822f" d="M12 0l3.1 7.6 8.2.6-6.3 5.3 2 8L12 17.2 5 21.5l2-8L.7 8.2l8.2-.6z"/></svg><svg width="22" height="21" viewBox="0 0 24 23"><path fill="#d5822f" d="M12 0l3.1 7.6 8.2.6-6.3 5.3 2 8L12 17.2 5 21.5l2-8L.7 8.2l8.2-.6z"/></svg>
    </div>
  </div>
</section>

<footer class="abs footer">
  <div class="abs social">
    <h3>Social Media</h3>
    <ul><li>tessapeonybrowsfinelinemaster</li><li>tessawynkelpeony</li><li>@tessabrows</li><li>tessabrows</li></ul>
  </div>
  <div class="abs subscribe">
    <h3>Subscribe &amp; Get 10% Off</h3>
    <p>More information and newslatter subscribe now</p>
  </div>
  <div class="abs email">Email address</div>
  <div class="btn" style="left:887px;top:152px;width:182px;height:50px;box-shadow:none">See More</div>
  <div class="abs rule"></div>
  <p class="abs copy">This website is created by TessaWynkelPeony | Copyright 2015</p>
</footer>

</body>
</html>
```